Creative/innovative law firm website

A law firm website that immediately looks different from other law firm websites. We like the color scheme (dark background with warm, neutral colors) and simple, organic logos (trees, leaves, etc.) of this website: https://nimbleway.law/

We'll be offering creative/innovative solutions to complex problems faced by state governments, industries, other law firms, and individuals. We're located in Montana (U.S.A.), and the outdoors is a huge part of our lives and identities.

We will need a home page, an "About Us" page with a separate subpage for each attorney (two attorneys), a blog or "Publications" page, a payment portal (which will integrate with Quindle), and a "Services" page.

```html
<!DOCTYPE html>
<html lang="en">
<head>
<meta charset="utf-8">
<title>Law Firm</title>
<link rel="stylesheet" href="https://fonts.googleapis.com/css2?family=Tinos&family=Poppins:wght@400;500;600&display=swap">
<style>
:root{
  --black:#0e0c0a;
  --panel:#211c17;
  --card:#2a241d;
  --card-line:#3d3429;
  --accent:#b8894f;
  --accent-soft:#d6b48a;
  --sand:#e9dcc8;
  --white:#fff;
  --serif:'Tinos',serif;
  --sans:'Poppins',sans-serif;
}
*{box-sizing:border-box;margin:0;padding:0}
html,body{width:1200px;height:3381px;overflow:hidden;background:var(--black);color:var(--white);font-family:var(--sans)}
.page{position:relative;width:1200px;height:3381px}
.abs{position:absolute}
.photo{position:absolute}

/* hero */
.hero{position:absolute;left:0;top:0;width:1200px;height:601px;background:linear-gradient(100deg,#1b1713 0%,#3b3027 38%,#4a3d31 62%,#201a15 100%)}
.brand{position:absolute;display:flex;align-items:center;gap:10px;font-family:var(--serif);font-size:44px;line-height:1;color:var(--white)}
.brand .mark{width:40px;height:40px;border-radius:50%;border:3px solid var(--accent-soft)}
.btn-pill{position:absolute;border-radius:30px;font-size:14.5px;font-weight:500;display:flex;align-items:center;justify-content:center;letter-spacing:.2px;white-space:nowrap}
.nav{position:absolute;top:86px;left:457px;display:flex;font-size:15.5px;font-weight:600;white-space:nowrap}
.nav span{margin-right:36px}
.hero h1{position:absolute;left:110px;top:222px;font-size:68px;font-family:var(--serif);font-weight:400;line-height:1}
.hero p{position:absolute;left:110px;top:303px;font-size:17.5px;line-height:29px;white-space:nowrap}
.dots{position:absolute;top:563px;left:565px;display:flex;gap:13px}
.dots i{width:13px;height:13px;border-radius:50%;border:2px solid var(--sand)}
.dots i.on{background:var(--sand)}

/* services */
.h2{position:absolute;width:1200px;text-align:center;font-family:var(--serif);font-size:41px;left:0;line-height:1.2}
.svc{position:absolute;width:211px;height:302px;background:var(--card);border:1px solid var(--card-line)}
.svc .photo{left:9px;top:9px;width:193px;height:136px}
.svc h3{position:absolute;top:158px;width:100%;text-align:center;font-family:var(--serif);font-weight:400;font-size:19.5px}
.svc p{position:absolute;top:189px;left:8px;right:8px;text-align:center;font-size:13.5px;line-height:26px}
.arrow{position:absolute;left:87px;bottom:-19px;width:37px;height:37px;border-radius:50%;background:var(--accent);display:flex;align-items:center;justify-content:center}

/* about */
.about{position:absolute;top:1205px;left:0;width:1200px;height:486px;background:var(--panel)}
.about .photo{left:568px;top:0;width:632px;height:486px;background:linear-gradient(135deg,#6b4a30,#a98866 45%,#cfc3b2 80%,#8f8270);clip-path:polygon(0 0,100% 0,100% 100%,76px 100%)}
.about .edge{position:absolute;left:566px;top:0}
.about h2{position:absolute;left:112px;top:92px;font-size:42px;font-family:var(--serif);font-weight:400;line-height:1.2}
.about p{position:absolute;left:112px;top:148px;width:436px;font-size:14px;line-height:28.3px;text-align:justify}

/* advantages */
.lead{position:absolute;width:1200px;left:0;text-align:center;font-size:18px;line-height:29px}
.adv{position:absolute;top:1912px;text-align:center;font-size:17.5px;line-height:26px;width:260px}
.adv svg{display:block;margin:0 auto 18px}

/* news */
.news{position:absolute;top:2253px;width:297px}
.news .photo{position:relative;width:297px;height:187px}
.meta{margin-top:14px;font-size:13.5px;display:flex;gap:20px;align-items:center;white-space:nowrap}
.meta span{display:flex;align-items:center;gap:6px}
.news h3{margin-top:10px;font-family:var(--serif);font-weight:400;font-size:20px;line-height:26px;white-space:nowrap}
.news p{margin-top:10px;font-size:14px;line-height:26px;white-space:nowrap}

/* consult */
.consult{position:absolute;top:2672px;left:0;width:1200px;height:390px;background:linear-gradient(180deg,#5a4a3a 0%,#4a3d30 55%,#0e0c0a 100%)}
.field{position:absolute;top:188px;width:235px;height:48px;background:#fff;color:#666;font-size:15.5px;padding-left:17px;display:flex;align-items:center}

/* footer */
.fcol{position:absolute;top:3138px;font-size:14px;line-height:28.5px;white-space:nowrap}
.fcol h4{font-size:15.5px;font-weight:600;margin-bottom:4px}
.soc{position:absolute;top:3179px;width:35px;height:35px;border-radius:50%;border:1px solid var(--sand)}
.payc{position:absolute;top:3225px;width:24px;height:15px;border-radius:2px}
</style>
</head>
<body>
<div class="page">

<section class="hero">
  <div class="photo" role="img" aria-label="Lawyer in glasses working on a laptop at a wooden desk" style="left:480px;top:0;width:720px;height:601px;background:radial-gradient(ellipse at 60% 45%,#6a5a48 0%,#3d3229 45%,transparent 75%)"></div>
  <div class="brand" style="left:110px;top:38px"><span class="mark"></span>LAW FIRM</div>
  <div class="btn-pill" style="left:681px;top:16px;width:243px;height:47px;background:var(--accent)">CONSULATION REQUEST</div>
  <div class="btn-pill" style="left:933px;top:16px;width:154px;height:47px;border:2px solid var(--sand)">PAY ONLINE</div>
  <div class="nav"><span>HOME</span><span>|</span><span>ABOUT</span><span>|</span><span>SERVICES</span><span>|</span><span>NEWS</span><span>|</span><span style="margin:0">CONTACT US</span></div>
  <h1>LAW FIRM</h1>
  <p>Lorem ipsum dolor sit amet, consectetur adipiscing<br>elit, sed do eiusmod tempor incidid</p>
  <div class="btn-pill" style="left:112px;top:375px;width:180px;height:50px;background:var(--accent);font-weight:600;font-size:16px">GET STARTED</div>
  <div class="dots"><i></i><i class="on"></i><i></i></div>
</section>

<div class="h2" style="top:683px">OUR SERVICES</div>

<div class="svc" style="left:111px;top:768px">
  <div class="photo" role="img" aria-label="Hands placing a small model house on a table" style="background:linear-gradient(135deg,#b8663a,#e2b08a 50%,#efe6da)"></div>
  <h3>Finibus Bonorum</h3><p>Sed ut peratis unde omnis iste naturor sit voluptatem accusantium dolore</p>
  <div class="arrow"><svg width="14" height="14" viewBox="0 0 14 14"><path d="M5 2l5 5-5 5" fill="none" stroke="#fff" stroke-width="2.4"/></svg></div>
</div>
<div class="svc" style="left:366px;top:802px">
  <div class="photo" role="img" aria-label="Hand signing documents with glasses on the desk" style="background:linear-gradient(135deg,#a49a8d,#ebe6de 50%,#bdb3a6)"></div>
  <h3>Finibus Bonorum</h3><p>Sed ut peratis unde omnis iste naturor sit voluptatem accusantium dolore</p>
  <div class="arrow"><svg width="14" height="14" viewBox="0 0 14 14"><path d="M5 2l5 5-5 5" fill="none" stroke="#fff" stroke-width="2.4"/></svg></div>
</div>
<div class="svc" style="left:622px;top:768px">
  <div class="photo" role="img" aria-label="Desk nameplate reading Immigration Law" style="background:linear-gradient(180deg,#2e2a25,#6b5542 60%,#c9a87c)"></div>
  <h3>Finibus Bonorum</h3><p>Sed ut peratis unde omnis iste naturor sit voluptatem accusantium dolore</p>
  <div class="arrow"><svg width="14" height="14" viewBox="0 0 14 14"><path d="M5 2l5 5-5 5" fill="none" stroke="#fff" stroke-width="2.4"/></svg></div>
</div>
<div class="svc" style="left:877px;top:802px">
  <div class="photo" role="img" aria-label="Two people exchanging papers across a desk" style="background:linear-gradient(135deg,#4a4036,#d9d1c5 55%,#f1ede6)"></div>
  <h3>Finibus Bonorum</h3><p>Sed ut peratis unde omnis iste naturor sit voluptatem accusantium dolore</p>
  <div class="arrow"><svg width="14" height="14" viewBox="0 0 14 14"><path d="M5 2l5 5-5 5" fill="none" stroke="#fff" stroke-width="2.4"/></svg></div>
</div>

<section class="about">
  <div class="photo" role="img" aria-label="Team of four colleagues smiling around a laptop in an office"></div>
  <svg class="edge" width="82" height="486" viewBox="0 0 82 486"><line x1="3" y1="0" x2="78" y2="486" stroke="#b8894f" stroke-width="5"/></svg>
  <h2>ABOUT LAW FIRM</h2>
  <p>Lorem ipsum dolor sit amet, consectetur adipiscing elit, sed do mod tempor incididunt ut labore et dolore magna aliqua. Quis ipsum suspendisse ultrices gravida. Risus commodo viverra maecenas accumsan lacus vel facilisis. Lorem ipsum dolor sit amet, etur iscing elit, sed do eiusmod tempor i ut labore et dolore magna aliqua.</p>
  <div class="btn-pill" style="left:112px;top:343px;width:153px;height:49px;border:2px solid var(--sand);font-size:16px;font-weight:600">READ MORE</div>
</section>

<div class="h2" style="top:1783px">STRATEGIC ADVANTAGE</div>
<div class="lead" style="top:1840px">Lorem ipsum dolor sit amet, consectetur adipiscing elit, iusmod tempor &nbsp;dolore magna aliqua.<br>Quis ipsum suspendisse ultrices gravida.</div>

<div class="adv" style="left:47px">
  <svg width="70" height="100" viewBox="0 0 70 100" fill="none" stroke="#b8894f" stroke-width="2.5"><circle cx="35" cy="28" r="12"/><path d="M35 16V4M23 22l-10-8M47 22l10-8M22 34H8M48 34h14"/><path d="M10 72h50v26H10z"/><path d="M18 72c0-12 8-18 17-18s17 6 17 18"/></svg>
  Top Tier Knowledge<br>&amp; Expertise</div>
<div class="adv" style="left:284px">
  <svg width="100" height="100" viewBox="0 0 100 100" fill="none" stroke="#b8894f" stroke-width="2.5"><path d="M20 10h50v80H20z"/><path d="M14 16h50v80"/><path d="M30 28h30M30 40h30M30 52h20"/><path d="M52 80l28-34 6 5-28 34-8 2z"/><path d="M4 96h92"/></svg>
  Client-Focused Approach to<br>Service Excellence</div>
<div class="adv" style="left:512px">
  <svg width="100" height="100" viewBox="0 0 100 100" fill="none" stroke="#b8894f" stroke-width="2.5"><path d="M37 4h26v26H37z"/><path d="M43 17l5 5 9-10"/><path d="M8 62l18-12 14 4 10-4 10 4 14-4 18 12"/><path d="M30 66l10 10 8-6 8 8 8-8 8 6"/><path d="M38 58l12 8 12-8"/></svg>
  A Commitment to<br>Diversity</div>
<div class="adv" style="left:705px">
  <svg width="80" height="100" viewBox="0 0 80 100" fill="none" stroke="#b8894f" stroke-width="2.5"><path d="M4 10l34-8v90L4 84z"/><circle cx="20" cy="40" r="6"/><path d="M20 46v14"/><path d="M44 16h14v72H44zM62 20h12v64H62z"/><path d="M48 28h6M48 40h6M48 52h6M66 32h4M66 44h4"/></svg>
  Attorney Access</div>
<div class="adv" style="left:903px">
  <svg width="96" height="100" viewBox="0 0 96 100" fill="none" stroke="#b8894f" stroke-width="2.5"><circle cx="48" cy="26" r="10"/><circle cx="48" cy="26" r="18" stroke-dasharray="7 5"/><path d="M6 96V62l10-18 8 4-6 18 14 14v16"/><path d="M90 96V62l-10-18-8 4 6 18-14 14v16"/></svg>
  Tech-led Solutions</div>

<div class="h2" style="top:2160px">LATEST NEWS</div>

<div class="news" style="left:111px">
  <div class="photo" role="img" aria-label="Smiling man at a meeting table with colleagues" style="background:linear-gradient(135deg,#55603f,#a9ad8c 50%,#4a4237)"></div>
  <div class="meta"><span><svg width="13" height="13" viewBox="0 0 13 13"><circle cx="6.5" cy="6.5" r="5" fill="none" stroke="#fff" stroke-width="1.4"/></svg>September 16-2019</span><span><svg width="13" height="13" viewBox="0 0 13 13"><circle cx="6.5" cy="6.5" r="5" fill="none" stroke="#fff" stroke-width="1.4"/></svg>0 Comments</span></div>
  <h3>Lorema ipsum dolor sit amet, ipsum<br>consectetur adipiscing</h3>
  <p>Lorem ipsum dolor sit amet, ciing elit, sed<br>do eiusmod temporLorem ipsum</p>
</div>
<div class="news" style="left:451px">
  <div class="photo" role="img" aria-label="Two colleagues laughing while reviewing papers" style="background:linear-gradient(135deg,#2e2a26,#c4583a 50%,#eae2d4)"></div>
  <div class="meta"><span><svg width="13" height="13" viewBox="0 0 13 13"><circle cx="6.5" cy="6.5" r="5" fill="none" stroke="#fff" stroke-width="1.4"/></svg>September 16-2019</span><span><svg width="13" height="13" viewBox="0 0 13 13"><circle cx="6.5" cy="6.5" r="5" fill="none" stroke="#fff" stroke-width="1.4"/></svg>0 Comments</span></div>
  <h3>Lorema ipsum dolor sit amet, ipsum<br>consectetur adipiscing</h3>
  <p>Lorem ipsum dolor sit amet, ciing elit, sed<br>do eiusmod temporLorem ipsum</p>
</div>
<div class="news" style="left:791px">
  <div class="photo" role="img" aria-label="Group of colleagues gathered around a document" style="background:linear-gradient(135deg,#4a4036,#c9a14a 45%,#a8443a)"></div>
  <div class="meta"><span><svg width="13" height="13" viewBox="0 0 13 13"><circle cx="6.5" cy="6.5" r="5" fill="none" stroke="#fff" stroke-width="1.4"/></svg>September 16-2019</span><span><svg width="13" height="13" viewBox="0 0 13 13"><circle cx="6.5" cy="6.5" r="5" fill="none" stroke="#fff" stroke-width="1.4"/></svg>0 Comments</span></div>
  <h3>Lorema ipsum dolor sit amet, ipsum<br>consectetur adipiscing</h3>
  <p>Lorem ipsum dolor sit amet, ciing elit, sed<br>do eiusmod temporLorem ipsum</p>
</div>

<section class="consult" role="img" aria-label="Cheering team with raised hands in a warm tinted backdrop">
  <div class="h2" style="top:112px">NEED A CONSULTATION?</div>
  <div class="field" style="left:112px">Name*</div>
  <div class="field" style="left:358px">Email*</div>
  <div class="field" style="left:605px">Phone*</div>
  <div class="field" style="left:852px">Message</div>
  <div class="btn-pill" style="left:487px;top:258px;width:226px;height:47px;background:#fff;color:var(--accent);font-size:16px;font-weight:600">SUBMIT FROM</div>
</section>

<div class="brand" style="left:112px;top:3162px"><span class="mark"></span>LAW FIRM</div>
<p class="abs" style="left:112px;top:3214px;font-size:14.5px;line-height:28.5px;white-space:nowrap">Lorem ipsum dolor sit amet, etur adipiscing<br>elit, sed do eiusmod teor incididunt ut labore<br>et dolore magna aliqua.</p>

<div class="fcol" style="left:512px"><h4>MAIN MENU</h4>Home<br>About<br>Services<br>News<br>Contact us</div>
<div class="fcol" style="left:708px"><h4>SUPPORT</h4>Contact<br>FAQ<br>Returns<br>Terms &amp; Conditions</div>
<div class="fcol" style="left:922px"><h4>SOCIAL</h4></div>
<div class="soc" style="left:922px"></div>
<div class="soc" style="left:965px"></div>
<div class="soc" style="left:1008px"></div>
<div class="soc" style="left:1052px"></div>
<div class="payc" style="left:918px;background:#8a6a45"></div>
<div class="payc" style="left:948px;background:#e9dcc8"></div>
<div class="payc" style="left:978px;background:#c9a227"></div>
<div class="payc" style="left:1008px;background:#f2ede4"></div>
<div class="payc" style="left:1038px;background:#a7876a"></div>
<div class="payc" style="left:1068px;background:#d9a94c"></div>

<div class="abs" style="left:111px;top:3332px;width:979px;height:1px;background:#4a4036"></div>
<div class="abs" style="left:0;top:3346px;width:1200px;text-align:center;font-size:14px">Copyright © 2021. All Rights Reserved</div>

</div>
</body>
</html>
```